Cleaning Service Company In need of Good Web presence.

The company is a cleaning service company which provides professional staff and service for cleaning. This is a project to build a site that is both solid and a strong recognition of our organization. It is supposed to show quality, cleanliness, professionalism. The use of images and art for imagery is all good just to have a site that is consistent and solid. There might be a chance to make stationary, logo and business cars if someone feels they can build a brand that is consistent. The image we are going for is clean solid and to stand out. Finally stationary should not be expensive to print.

Current logo is attached and can be used or can be made more creative.

Target Market(s)

Corporate and Government entities, that will feel that this company has a brand that sets it apart from the rest. The company is new so the modification of the logo will not be an issue if a more solid brand come out of this project. The idea is to have a clean consistent product that stands our from others in terms of website, stationary, etc

Industry/Entity Type

Cleaning Service

Contact Information for Business Card

P.O.Box 41967
Riffa
Kingdom of Bahrain

Logo Text

Maple Ridge Solutions

Number of Pages Required

4 page

Font styles to use
Sans Serif

Colors
abd036
cadf82
eaf2ce
9bcb3b

Requirements
Must have
• Green Color to be used in order to stick to the name. Also the creativity and boldness in an elegant manner.
Nice to have
• Arabic name of company
• نوفا بلو للحلول ذ.م.م
• if cannot be put at least make a location should be chosen
• Also could be a bit of 3D given to the logo if it could stay elegent.
Should not have
• Should not show people cleaning.

```html
<!DOCTYPE html>
<html lang="en">
<head>
<meta charset="utf-8">
<title>Maple Ridge Solutions – Professional Cleaning Services</title>
<link href="https://fonts.googleapis.com/css2?family=Nunito+Sans:ital,wght@0,400;0,700;0,800;1,700&family=Open+Sans:wght@400;600;700&display=swap" rel="stylesheet">
<style>
:root{
  --green:#9bcb3b;
  --green-strong:#8cc63f;
  --green-dark:#6f9f23;
  --green-soft:#cadf82;
  --green-pale:#eaf2ce;
  --ink:#2b2b2b;
  --text:#4a4a4a;
  --rule:#cfcfcf;
  --frame:#e6e6e6;
  --nav-bg:#ececec;
  --white:#ffffff;
}
*{margin:0;padding:0;box-sizing:border-box}
html,body{width:1200px;height:2659px;overflow:hidden}
body{background:var(--frame);position:relative;font-family:"Open Sans",sans-serif;color:var(--text)}
.page{position:absolute;left:14px;top:9px;width:1172px;height:2636px;background:var(--white);overflow:hidden}
.abs{position:absolute}
.top-line{left:0;top:0;width:100%;height:4px;background:var(--green)}

/* contact bar */
.contact-bar{left:635px;top:9px;width:508px;height:39px;background:var(--green);border-radius:0 0 8px 8px;display:flex;align-items:center;padding:0 22px;gap:30px;color:var(--white);font:700 13px "Nunito Sans",sans-serif}
.contact-bar .item{display:flex;align-items:center;gap:9px}
.icon-dot{width:22px;height:22px;border-radius:50%;background:var(--white);display:flex;align-items:center;justify-content:center}
.social{margin-left:auto;display:flex;gap:5px}
.social span{width:20px;height:20px;border-radius:50%;border:2px solid var(--white)}

/* nav */
.nav{left:0;top:117px;width:100%;height:35px;background:var(--nav-bg)}
.nav-links{position:absolute;left:523px;top:0;height:35px;display:flex;font:700 14px "Nunito Sans",sans-serif;color:var(--ink)}
.nav-links a{display:flex;align-items:center;justify-content:center;height:35px;color:var(--ink);text-decoration:none}
.nav-links a.active{background:var(--green);color:var(--white)}

.hero{left:0;top:152px;width:100%;height:518px;background:linear-gradient(100deg,#d9d4cc 0%,#eeeeec 30%,#f2f2f2 55%,#9a9a9a 72%,#2d3035 85%,#dcdcdc 100%)}

.brand-badge{width:188px;height:188px;border-radius:50%;background:var(--white);border:6px solid var(--green);display:flex;flex-direction:column;align-items:center;justify-content:center;text-align:center;gap:10px;box-shadow:0 3px 8px rgba(0,0,0,.15)}
.brand-badge .mark{width:34px;height:34px;border-radius:50%;background:var(--green)}
.brand-badge .name{font:800 18px/1.15 "Nunito Sans",sans-serif;color:var(--green-dark);width:130px}

/* banner */
.banner{left:0;top:670px;width:1172px;height:140px}
.banner-title{left:0;top:699px;width:1172px;text-align:center;color:var(--white);font:800 25px "Nunito Sans",sans-serif;letter-spacing:.3px}

/* section heading */
.section-head{left:0;width:1172px;display:flex;align-items:center;justify-content:center;gap:18px;font:800 25px "Nunito Sans",sans-serif;color:var(--ink)}
.section-head .rule{width:92px;height:1px;background:var(--rule)}
.section-head .dot{width:28px;height:28px;border-radius:50%;background:var(--green)}
.section-head .accent{color:var(--green-dark)}
.section-head.on-green{color:var(--white)}
.section-head.on-green .rule{background:rgba(255,255,255,.55)}
.section-head.on-green .dot{background:var(--white)}

.about-text{left:60px;top:912px;width:1052px;text-align:center;font-size:14.5px;line-height:22px;color:var(--text)}
.btn{left:491px;top:1065px;width:190px;height:42px;background:var(--green);border-radius:6px;color:var(--white);font:800 17px "Nunito Sans",sans-serif;display:flex;align-items:center;justify-content:center;box-shadow:0 10px 10px -6px rgba(0,0,0,.35)}

/* services */
.services-bg{left:0;top:1168px;width:1172px;height:752px}
.service{color:var(--white);font-size:14.5px;line-height:21px}
.service h3{font:800 15px "Nunito Sans",sans-serif;text-transform:uppercase;margin-bottom:2px}
.diagram{left:0;top:1168px;width:1172px;height:752px}

/* testimonials */
.quote-box{left:241px;top:2042px;width:692px;height:142px;border:1px solid #cfcfcf;border-radius:8px;background:#f6f6f6;padding:16px 30px 0 56px;font-size:14.5px;line-height:20px;color:var(--text)}
.q-mark{font:800 50px/1 "Nunito Sans",sans-serif;color:#555}
.quote-tail{left:268px;top:2183px;width:18px;height:18px;background:#f6f6f6;border-right:1px solid #cfcfcf;border-bottom:1px solid #cfcfcf;transform:rotate(45deg) translate(-9px,-2px)}
.author{left:243px;top:2202px;font:italic 700 17px "Nunito Sans",sans-serif;color:var(--ink)}
.dots{left:556px;top:2249px;display:flex;gap:4px}
.dots span{width:12px;height:12px;border-radius:50%;border:1.5px solid #777}
.dots span.on{background:var(--green);border-color:var(--green)}

/* footer */
.footer{left:0;top:2334px;width:1172px;height:268px;background:var(--green)}
.footer-col{color:var(--white)}
.footer-col h4{font:800 15px "Nunito Sans",sans-serif;padding-bottom:10px;border-bottom:1px solid rgba(255,255,255,.8);margin-bottom:14px}
.footer-col ul{list-style:none;font:700 12.5px/20px "Nunito Sans",sans-serif}
.f-line{display:flex;gap:10px;font:700 12.5px/17px "Nunito Sans",sans-serif;margin-bottom:22px}
.f-ico{flex:none;width:19px;height:19px;border-radius:50%;border:1.5px solid var(--white);display:flex;align-items:center;justify-content:center}
.field{width:283px;border:1.5px solid var(--white);border-radius:3px;color:var(--white);font:700 9px "Nunito Sans",sans-serif;padding:4px 6px;margin-bottom:6px}
.submit{width:96px;height:26px;background:#2b2b2b;color:var(--white);font:800 12px "Nunito Sans",sans-serif;display:flex;align-items:center;justify-content:center;border-radius:2px}
.copyright{left:0;top:2602px;width:1172px;height:34px;display:flex;align-items:center;justify-content:center;font:700 11px "Nunito Sans",sans-serif;color:var(--ink)}
</style>
</head>
<body>
<div class="page">
  <div class="abs top-line"></div>

  <div class="abs hero" role="img" aria-label="Photo of a bright, clean living room with a wooden chair, dining table and dark sofa"></div>

  <div class="abs contact-bar">
    <div class="item"><span class="icon-dot"><svg width="12" height="12" viewBox="0 0 24 24"><path d="M6.6 10.8a15 15 0 0 0 6.6 6.6l2.2-2.2c.3-.3.7-.4 1-.2 1.1.4 2.3.6 3.6.6.6 0 1 .4 1 1V20c0 .6-.4 1-1 1A17 17 0 0 1 3 4c0-.6.4-1 1-1h3.5c.6 0 1 .4 1 1 0 1.3.2 2.5.6 3.6.1.3 0 .7-.2 1z" fill="#9bcb3b"/></svg></span>555.410.2288</div>
    <div class="item"><span class="icon-dot"><svg width="12" height="10" viewBox="0 0 24 18"><rect x="1" y="1" width="22" height="16" rx="2" fill="none" stroke="#9bcb3b" stroke-width="2.5"/><path d="M1 2l11 8 11-8" fill="none" stroke="#9bcb3b" stroke-width="2.5"/></svg></span>info@mapleridgesolutions.com</div>
    <div class="social"><span></span><span></span><span></span></div>
  </div>

  <nav class="abs nav">
    <div class="nav-links">
      <a class="active" style="width:99px">HOME</a>
      <a style="width:114px">ABOUT US</a>
      <a style="width:128px">OUR SERVICES</a>
      <a style="width:134px">TESTIMONIALS</a>
      <a style="width:112px">CONTACT</a>
    </div>
  </nav>

  <div class="abs brand-badge" style="left:30px;top:26px">
    <span class="mark"></span>
    <span class="name">Maple Ridge Solutions</span>
  </div>

  <svg class="abs banner" viewBox="0 0 1172 140" preserveAspectRatio="none">
    <polygon points="0,0 1172,0 1172,92 586,136 0,92" fill="#9bcb3b"/>
  </svg>
  <div class="abs banner-title">THE TRUSTED NAME FOR PROFESSIONAL CLEANING SERVICES IN BAHRAIN</div>

  <div class="abs section-head" style="top:855px"><span class="rule"></span><span class="dot"></span><span>ABOUT <span class="accent">US</span></span><span class="rule"></span></div>
  <p class="abs about-text">Lorem ipsum dolor sit amet, consectetuer adipiscing elit, sed diam nonummy nibh euismod tincidunt ut laoreet dolore magna aliquam erat volutpat. Ut wisi enim ad minim veniam, quis nostrud exerci tation ullamcorper suscipit lobortis nisl ut aliquip ex ea commodo consequat. Duis autem vel eum iriure dolor in hendrerit in vulputate velit esse molestie consequat, vel illum dolore eu feugiat nulla facilisis at vero eros et accumsan et iusto odio dignissim qui blandit praesent luptatum zzril delenit augue duis dolore te feugait nulla facilisi. Nam liber tempor cum soluta nobis eleifend option congue nihil imperdiet doming id quod mazim placerat facer possim assum.</p>
  <div class="abs btn">Learn More</div>

  <svg class="abs services-bg" viewBox="0 0 1172 752" role="img" aria-label="Photo of a modern house exterior with garden, tinted green">
    <defs>
      <linearGradient id="servicesTint" x1="0" y1="0" x2="0" y2="1">
        <stop offset="0" stop-color="#a9d15a"/>
        <stop offset=".55" stop-color="#96c243"/>
        <stop offset="1" stop-color="#7faf2e"/>
      </linearGradient>
    </defs>
    <polygon points="0,0 586,42 1172,0 1172,692 586,752 0,692" fill="url(#servicesTint)"/>
  </svg>

  <div class="abs section-head on-green" style="top:1274px"><span class="rule"></span><span class="dot"></span><span>OUR SERVICES</span><span class="rule"></span></div>

  <div class="abs service" style="left:441px;top:1353px;width:300px"><h3>Commercial</h3>Lorem ipsum dolor sit amet, consectetuer adipiscing elit, sed diam nonummy nibh euismod tincidunt ut laoreet dolore magna aliquam erat volutpat.</div>
  <div class="abs service" style="left:36px;top:1541px;width:300px"><h3>Residential</h3>Lorem ipsum dolor sit amet, consectetuer adipiscing elit, sed diam nonummy nibh euismod tincidunt ut laoreet dolore magna aliquam erat volutpat.</div>
  <div class="abs service" style="left:847px;top:1541px;width:300px"><h3>Holiday Homes</h3>Lorem ipsum dolor sit amet, consectetuer adipiscing elit, sed diam nonummy nibh euismod tincidunt ut laoreet dolore magna aliquam erat volutpat.</div>

  <svg class="abs diagram" viewBox="0 0 1172 752">
    <g stroke="#ffffff" stroke-width="2.5" fill="none">
      <path d="M445,493 Q585,407 725,493"/>
      <line x1="585" y1="409" x2="585" y2="408"/>
      <line x1="585" y1="408" x2="585" y2="409"/>
      <line x1="445" y1="493" x2="411" y2="456"/>
      <line x1="725" y1="493" x2="759" y2="456"/>
      <line x1="585" y1="447" x2="585" y2="408"/>
      <line x1="585" y1="408" x2="585" y2="496"/>
    </g>
    <g fill="#9bcb3b" stroke="#ffffff" stroke-width="2.5">
      <circle cx="445" cy="493" r="7"/><circle cx="585" cy="449" r="7"/><circle cx="725" cy="493" r="7"/>
    </g>
    <g fill="#9bcb3b" stroke="#ffffff" stroke-width="5">
      <circle cx="392" cy="418" r="44"/><circle cx="585" cy="362" r="44"/><circle cx="776" cy="418" r="44"/>
    </g>
    <!-- residential: low house -->
    <g fill="#ffffff">
      <polygon points="368,418 392,400 416,418"/><rect x="372" y="418" width="40" height="20"/>
      <rect x="388" y="426" width="8" height="12" fill="#9bcb3b"/>
    </g>
    <!-- commercial: office block -->
    <g fill="#ffffff">
      <rect x="567" y="340" width="36" height="44"/>
      <g fill="#9bcb3b"><rect x="573" y="347" width="6" height="6"/><rect x="582" y="347" width="6" height="6"/><rect x="591" y="347" width="6" height="6"/><rect x="573" y="357" width="6" height="6"/><rect x="582" y="357" width="6" height="6"/><rect x="591" y="357" width="6" height="6"/><rect x="581" y="372" width="8" height="12"/></g>
    </g>
    <!-- holiday home -->
    <g fill="#ffffff">
      <polygon points="754,418 776,396 798,418"/><rect x="759" y="418" width="34" height="22"/>
      <rect x="772" y="426" width="8" height="14" fill="#9bcb3b"/>
    </g>
  </svg>

  <div class="abs brand-badge" style="left:496px;top:1630px;width:178px;height:178px"><span class="mark"></span><span class="name">Maple Ridge Solutions</span></div>

  <div class="abs section-head" style="top:1972px"><span class="rule" style="width:110px"></span><span class="dot"></span><span>TESTIMONIALS</span><span class="rule" style="width:110px"></span></div>

  <div class="abs quote-box">
    <span class="abs q-mark" style="left:16px;top:10px">&ldquo;</span>
    Lorem ipsum dolor sit amet, consectetuer adipiscing elit, sed diam nonummy nibh euismod tincidunt ut laoreet dolore magna aliquam erat volutpat. Ut wisi enim ad minim veniam, quis nostrud exercitation ullamcorper suscipit lobortis nisl ut aliquip ex ea commodo consequat. Duis autem vel eum iriure dolor in hendrerit in vulputate velit esse molestie consequat, vel illum dolore eu feugiat nulla facilisis at vero.
    <span class="q-mark" style="position:relative;top:18px;margin-left:6px">&rdquo;</span>
  </div>
  <div class="abs quote-tail"></div>
  <div class="abs author">Mara Ellison</div>
  <div class="abs dots"><span class="on"></span><span></span><span></span><span></span></div>

  <footer class="abs footer"></footer>
  <div class="abs brand-badge" style="left:37px;top:2313px;width:160px;height:160px"><span class="mark" style="width:28px;height:28px"></span><span class="name" style="font-size:16px;width:110px">Maple Ridge Solutions</span></div>

  <div class="abs footer-col" style="left:307px;top:2365px;width:150px">
    <h4>QUICK LINKS</h4>
    <ul><li>HOME</li><li>ABOUT US</li><li>OUR SERVICES</li><li>TESTIMONIALS</li><li>CONTACT US</li></ul>
  </div>
  <div class="abs footer-col" style="left:494px;top:2365px;width:200px">
    <h4>CONTACT</h4>
    <div class="f-line"><span class="f-ico"><svg width="9" height="11" viewBox="0 0 12 16"><path d="M6 0a6 6 0 0 0-6 6c0 4.5 6 10 6 10s6-5.5 6-10a6 6 0 0 0-6-6zm0 8.5A2.5 2.5 0 1 1 6 3.5a2.5 2.5 0 0 1 0 5z" fill="#fff"/></svg></span><span>MAPLE RIDGE SOLUTIONS W.L.L<br>P.O.Box 41967<br>RIFFA, BAHRAIN</span></div>
    <div class="f-line"><span class="f-ico"><svg width="10" height="10" viewBox="0 0 24 24"><path d="M6.6 10.8a15 15 0 0 0 6.6 6.6l2.2-2.2c.3-.3.7-.4 1-.2 1.1.4 2.3.6 3.6.6.6 0 1 .4 1 1V20c0 .6-.4 1-1 1A17 17 0 0 1 3 4c0-.6.4-1 1-1h3.5c.6 0 1 .4 1 1 0 1.3.2 2.5.6 3.6.1.3 0 .7-.2 1z" fill="#fff"/></svg></span><span>555-410-2288</span></div>
    <div class="f-line"><span class="f-ico"><svg width="10" height="8" viewBox="0 0 24 18"><rect x="1" y="1" width="22" height="16" rx="2" fill="none" stroke="#fff" stroke-width="2.5"/><path d="M1 2l11 8 11-8" fill="none" stroke="#fff" stroke-width="2.5"/></svg></span><span>info@mapleridgesolutions.com</span></div>
  </div>
  <div class="abs footer-col" style="left:776px;top:2365px;width:283px">
    <h4>SEND A MESSAGE</h4>
    <div class="field" style="height:27px">Name</div>
    <div class="field" style="height:27px">Email</div>
    <div class="field" style="height:60px">Message</div>
    <div class="submit">SUBMIT</div>
  </div>

  <div class="abs copyright">COPYRIGHT © 2017 MAPLE RIDGE SOLUTIONS W.L.L. ALL RIGHTS RESERVED.</div>
</div>
</body>
</html>
```